Regional Showdown Flyer for Holiday Program

Need a one page flyer, can be back to front or one page, ensuring you can fit all information, colourful, aimed at a market of 8-13 year old boys and girls.
The flyer needs to be noticed, needs to have certain information on it and needs to be Autralian Rule Football orientated.
Have uploaded file so you can understand the style (not content), style of flyer I am looking at getting submitted.

Target Market(s)

8-13 year old boys and girls and their parents.

Requirements
Must have
• Regional Showdown Event
• Price for Regional Showdown Day will be $85
• Strictly Limited Places, only the best footballers should enter this challenge
• Inaugural event, be the first Regional Showdown Winner for your age!
• Do you love a challenge! Put yourself to the test!
• Are you up to it - Water Slide Goal Kicking Contest! The fastest kick in the West (tested by our very own speed gun)! Can you survive the Footy Titan Trail or Last One Standing Goal Kicking! These challenges are crazy are super fun!
• If you think you can deliver on the big stage then this is for YOU!
• All District age winners will receive prizes, awards and the adulation from all their peers!
• Year's 3-5 from 9am to 12pm
• Year's 6-8 from 1-4pm
• All challengers compete against their own age
• Lunch Provided
• Monday 16th April - Upper Tarrowby Regional Showdown Day at Tarrowby Oval
• Tuesday 17th April - North Tarrowby Regional Showdown Day at Kilmorna Reserve
• Wednesday 18th April - Yarlo Regional Showdown Day - Dunhaven Football Club
• Every Challenge Participant receives a District Football!
• Need to put all 3 District Football Logos on the bottom of the flyer, logos attached at bottom.
Nice to have
• Plenty of colour, if you can fit all information on one page that would be fine
Should not have
• Dull, boring, any footballs should be Aussie Rules footballs not NFL or soccer

```html
<!DOCTYPE html>
<html lang="en">
<head>
<meta charset="utf-8">
<title>Regional Showdown Flyer – Front and Back</title>
<link rel="stylesheet" href="https://fonts.googleapis.com/css2?family=Lilita+One&family=Fjalla+One&display=swap">
<style>
  :root {
    --stage: #2f4f80;
    --page-dark: #262323;
    --title-red: #e5344c;
    --title-edge: #ffffff;
    --price-yellow: #e9d84c;
    --hot-pink: #f54fb0;
    --pink-dark: #c23a8e;
    --mint: #5ad3ae;
    --mint-dark: #3aa886;
    --text-dark: #1c1a1a;
    --text-yellow: #f5e84a;
    --logo-navy: #23356f;
    --logo-teal: #1f9a8a;
    --logo-red: #d6202a;
    --outline: #7a5bc4;
  }
  * { box-sizing: border-box; margin: 0; padding: 0; }
  html, body { width: 1200px; height: 1200px; overflow: hidden; }
  body {
    background: var(--stage);
    font-family: "Fjalla One", "Arial Narrow", sans-serif;
    position: relative;
  }
  .spread {
    position: absolute; left: 0; top: 175px;
    width: 1200px; height: 849px;
    display: flex;
  }
  .flyer {
    position: relative; width: 600px; height: 849px;
    overflow: hidden; background: #fff;
  }
  .flyer + .flyer { border-left: 1px solid #555; }
  .flyer-body {
    position: absolute; left: 0; top: 0; width: 600px; height: 742px;
    background: var(--page-dark); overflow: hidden;
  }
  .flame-art {
    position: absolute; inset: 0;
    background:
      radial-gradient(ellipse 260px 150px at 230px 330px, rgba(210,110,90,.85), rgba(210,110,90,0) 70%),
      radial-gradient(ellipse 200px 380px at 470px 380px, rgba(240,200,40,.75), rgba(240,200,40,0) 70%),
      radial-gradient(ellipse 320px 160px at 300px 200px, rgba(200,20,70,.75), rgba(200,20,70,0) 70%),
      linear-gradient(160deg, rgba(0,0,0,0) 45%, rgba(240,110,40,.45) 60%, rgba(0,0,0,0) 75%),
      linear-gradient(200deg, rgba(250,215,60,.55) 0%, rgba(0,0,0,0) 35%);
  }
  .event-title {
    position: absolute; left: 0; right: 0; top: 38px;
    text-align: center; font-family: "Lilita One", sans-serif;
    color: var(--title-red); line-height: .95;
    text-shadow: 0 3px 0 var(--title-edge), 0 6px 0 #d9d0d6, 0 8px 6px rgba(0,0,0,.5);
    transform: rotate(-3deg);
  }
  .event-title .title-main { display: block; font-size: 60px; letter-spacing: -1px; }
  .event-title .title-sub { display: block; font-size: 66px; margin-top: 4px; }

  .panel { position: absolute; }
  .panel::after {
    content: ""; position: absolute; inset: -8px -10px;
    border: 1px solid var(--outline); transform: rotate(-1.5deg); pointer-events: none;
  }
  .price-panel {
    left: 306px; top: 245px; width: 258px; height: 88px;
    background: var(--price-yellow); text-align: center;
    font-family: "Lilita One", sans-serif; color: var(--title-red);
    transform: rotate(-1deg);
  }
  .price-panel .price-lead { font-size: 24px; margin-top: 4px; display: block; }
  .price-panel .price-amount { font-size: 58px; line-height: .95; display: block; }
  .dollar-badge {
    position: absolute; left: 220px; top: 253px; width: 80px; height: 80px;
    border-radius: 50%; background: #fff; border: 5px solid var(--price-yellow);
    color: var(--title-red); font-family: "Lilita One", sans-serif;
    font-size: 54px; line-height: 70px; text-align: center;
  }
  .pink-panel {
    background: var(--hot-pink); color: var(--text-yellow);
    font-size: 12px; line-height: 1.35;
  }
  .front .pink-panel { left: 40px; top: 385px; width: 300px; height: 108px; padding: 12px 10px; }
  .medal-art {
    position: absolute; left: 344px; top: 388px; width: 108px; height: 108px;
    border-radius: 50%; border: 7px solid var(--hot-pink);
    background: radial-gradient(circle at 50% 55%, #f5b73a 0 38%, #fbe6d9 40% 100%);
  }
  .mint-panel {
    background: var(--mint); color: var(--text-dark); text-align: center;
  }
  .front .mint-panel {
    left: 224px; top: 565px; width: 336px; height: 108px;
    font-size: 12.5px; line-height: 1.5; padding: 12px 10px;
  }
  .slide-art {
    position: absolute; left: 116px; top: 571px; width: 100px; height: 100px;
    border-radius: 50%; border: 5px solid var(--mint-dark);
    background: radial-gradient(circle, #f4f0e6 0 30%, #f07a2a 32% 55%, #ffffff 57%);
  }
  .back .info-panel {
    left: 120px; top: 205px; width: 416px; height: 128px;
    background: var(--price-yellow); color: var(--text-dark);
    font-size: 11px; line-height: 1.9; padding: 14px 10px;
  }
  .back .pink-panel { left: 32px; top: 377px; width: 390px; height: 136px; padding: 16px 12px; font-size: 11.5px; line-height: 1.85; }
  .back .mint-panel {
    left: 116px; top: 569px; width: 418px; height: 136px;
    font-size: 16px; line-height: 1.9; padding-top: 36px;
  }
  .ribbon-tail { position: absolute; }

  .club-strip {
    position: absolute; left: 0; top: 742px; width: 600px; height: 107px;
    background: #fff; display: flex; align-items: center; justify-content: space-around;
    padding: 0 24px;
  }
  .club-mark {
    display: flex; align-items: center; gap: 8px;
    font-family: "Lilita One", sans-serif; font-size: 17px; line-height: 1;
  }
  .club-mark .mark-dot { width: 26px; height: 26px; border-radius: 50%; }
  .club-marlin { color: var(--logo-navy); }
  .club-marlin .mark-dot { background: var(--logo-navy); }
  .club-yarlo { color: var(--logo-teal); }
  .club-yarlo .mark-dot { background: var(--logo-teal); }
  .club-kelpie { color: var(--logo-red); }
  .club-kelpie .mark-dot { background: var(--logo-red); }
</style>
</head>
<body>
<main class="spread">

  <section class="flyer front" aria-label="Flyer front">
    <div class="flyer-body">
      <div class="flame-art" role="img" aria-label="Aussie Rules football streaking through red, orange and yellow flames"></div>
      <h1 class="event-title"><span class="title-main">Regional Showdown</span><span class="title-sub">Event</span></h1>

      <div class="dollar-badge">$</div>
      <div class="panel price-panel">
        <span class="price-lead">FOR ONLY</span>
        <span class="price-amount">$85</span>
      </div>

      <div class="panel pink-panel">
        Strictly Limited Places, only the best footballers should enter this challenge.<br>
        Inaugural event, be the first Regional Showdown Winner for your age!<br>
        Do you love a challenge! Put yourself to the test!
      </div>
      <svg class="ribbon-tail" style="left:50px;top:486px" width="56" height="46" viewBox="0 0 56 46"><polygon points="6,0 54,0 0,46" fill="var(--pink-dark)"/></svg>
      <div class="medal-art" role="img" aria-label="Gold first place medal"></div>

      <svg class="ribbon-tail" style="left:500px;top:526px" width="60" height="46" viewBox="0 0 60 46"><polygon points="8,46 60,46 48,0" fill="var(--mint-dark)"/></svg>
      <div class="panel mint-panel">
        Are you up to it - Water Slide Goal Kicking Contest! The fastest kick in the West (tested by our very own speed gun)! Can you survive the Footy Titan Trail or Last One Standing Goal Kicking! These challenges are crazy are super fun!
      </div>
      <div class="slide-art" role="img" aria-label="Inflatable goal kicking water slide"></div>
    </div>
    <footer class="club-strip">
      <div class="club-mark club-marlin"><span class="mark-dot"></span>MARLIN DISTRICT</div>
      <div class="club-mark club-yarlo"><span class="mark-dot"></span>YARLO DISTRICT</div>
      <div class="club-mark club-kelpie"><span class="mark-dot"></span>KELPIE DISTRICT</div>
    </footer>
  </section>

  <section class="flyer back" aria-label="Flyer back">
    <div class="flyer-body">
      <div class="flame-art" role="img" aria-label="Aussie Rules football streaking through red, orange and yellow flames"></div>
      <h2 class="event-title"><span class="title-main">Regional Showdown</span><span class="title-sub">Event</span></h2>

      <div class="panel info-panel">
        If you think you can deliver on the big stage then this is for YOU!<br>
        All District age winners will receive prizes, awards and the adulation from all their peers!<br>
        Year's 3-5 from 9am to 12pm<br>
        Year's 6-8 from 1-4pm<br>
        All challengers compete against their own age
      </div>
      <svg class="ribbon-tail" style="left:490px;top:330px" width="60" height="60" viewBox="0 0 60 60"><polygon points="0,0 50,0 60,60" fill="#d8c63a"/></svg>

      <div class="panel pink-panel">
        Lunch Provided<br>
        Monday 16th April - Upper Tarrowby Regional Showdown Day at Tarrowby Oval<br>
        Tuesday 17th April - North Tarrowby Regional Showdown Day at Kilmorna Reserve<br>
        Wednesday 18th April - Yarlo Regional Showdown Day - Dunhaven Football Club
      </div>
      <svg class="ribbon-tail" style="left:56px;top:506px" width="70" height="56" viewBox="0 0 70 56"><polygon points="10,0 70,0 0,56" fill="var(--pink-dark)"/></svg>

      <svg class="ribbon-tail" style="left:466px;top:526px" width="60" height="46" viewBox="0 0 60 46"><polygon points="8,46 60,46 48,0" fill="var(--mint-dark)"/></svg>
      <div class="panel mint-panel">
        Every Challenge Participant receives a<br>District Football!
      </div>
    </div>
    <footer class="club-strip">
      <div class="club-mark club-marlin"><span class="mark-dot"></span>MARLIN DISTRICT</div>
      <div class="club-mark club-yarlo"><span class="mark-dot"></span>YARLO DISTRICT</div>
      <div class="club-mark club-kelpie"><span class="mark-dot"></span>KELPIE DISTRICT</div>
    </footer>
  </section>

</main>
</body>
</html>
```